依頼詳細
「仙台箪笥」は本来すべてが「手しごと」で作られたものを言います。しかし、近年は工場の機械で大量生産されたものを「仙台箪笥」として販売する企業が増えてきており、「本物」を作る職人達は価格競争で負けてしまいます。そんな中でも、柴崎庵では全ての工程を手しごとで行い、愚直に仙台箪笥を作り続けてきました。今のまま「安かろう、良かろう」の精神で仙台箪笥を販売する企業や、それを購入する消費者が増え続けてしまっては、江戸時代から培われてきた仙台の伝統が途絶えてしまいます。本チラシのデザインでは、そんな時代に警笛を鳴らすようなメッセージを込めて頂きたいと考えております。柴崎庵の代表・柴崎守氏からのメッセージや仙台箪笥の歴史を説明する資料を添付します。そちらを参考に、本物の箪笥の価値を伝えるデザインをして下さった方を採用とさせて頂きます。柴崎氏からの要望は2つあり、「『ずいぶんお堅い感じね』と言われるようなもの』」「伝統工芸をずっと続けてやっているんだなというイメージ」を意識してほしいとのことです。その他、何か質問があればどうぞお気軽にお問い合わせくださいませ。Mail→tokoharuwen@mailbox-demo.jp
記載項目
工房名/仙台箪笥 柴崎庵
住所/添付資料
電話番号/添付資料
ホームページURL・QRコード/現在HPリニューアル中のため、リニューアル完了後にこちらで入れ込みます。入れるスペースを分かるようにしておいてください。
キャッチコピー/デザインに合わせ、「依頼詳細」にある説明を参考に、心に刺さるコピーを入れてください。
写真/添付資料にある、柴崎守氏の写真と仙台箪笥の写真を中心に上手く組み合わせてデザインしてください。

〜コピー参考例〜
(コピーが浮かばなかった場合は、こちらのコピーの中から選んで入れてください。)

・一〇〇年先に繋ぎたい、一〇〇年前の財産
・本物しか作らない、「手しごと」の心
サイズ
A4
ページ数
片面
希望イメージ
シンプル 複雑
単色 カラフル
暗い 明るい
日常 高級
遊び心 厳粛
未来的 伝統的
女性的 男性的
希望する色
仙台箪笥の色にあった色を基調としてください。
納品ファイル
• イラストレーター形式 (.ai)
補足説明
現在リニューアル中ですが、こちらが現在の「柴崎庵」のホームページです。
http://homepage5.example-host.jp/shibasakian/
→ページ左上にあるロゴを使用できれば、デザインの中に入れ込んでほしいです
参考映像
https://www.videoshare-demo.jp/watch?v=Qw3rTz8LmNp
https://www.videoshare-demo.jp/watch?v=Vb6yHs2KoRd

柴崎氏ご本人に選んで頂きました。

この度は多数のご応募、誠にありがとうございました。どの作品も素晴らしいもので、一つに選ぶのが非常に難しかったです。またの機会にも、どうぞご応募頂ければ幸いです。宜しくお願い致します。

```html
<!DOCTYPE html>
<html lang="ja">
<head>
<meta charset="utf-8">
<title>仙台箪笥 柴崎庵 手しごと</title>
<link rel="stylesheet" href="https://fonts.googleapis.com/css2?family=Shippori+Mincho:wght@400;700;800&family=Yuji+Syuku&display=swap">
<style>
:root{
  --paper:#f1efe8;
  --ink:#2a2120;
  --red:#b3262b;
  --tansu:#4a1518;
  --iron:#1c1a1a;
  --line:#cfc9bb;
}
*{margin:0;padding:0;box-sizing:border-box}
html,body{width:846px;height:1200px;overflow:hidden;background:var(--paper)}
body{position:relative;font-family:"Shippori Mincho",serif;color:var(--ink)}
.vertical{writing-mode:vertical-rl;text-orientation:mixed}
.photo{position:absolute;display:block}
.photo-urushi{left:0;top:0;width:325px;height:118px;background:linear-gradient(135deg,#5b4a40,#2b2322 60%,#6b5a4c)}
.photo-kanagu{left:372px;top:0;width:205px;height:118px;background:linear-gradient(160deg,#8f7a68,#c9b8a4 55%,#6e5d50)}
.photo-mokkou{left:660px;top:0;width:186px;height:118px;background:linear-gradient(200deg,#d8cbb5,#a88d70 60%,#e6dccb)}
.craft-label{position:absolute;color:var(--red);font-weight:700;font-size:26px;letter-spacing:4px;line-height:1}
.label-urushi{left:334px;top:50px}
.label-kanagu{left:585px;top:32px}
.label-mokkou{left:624px;top:20px}
.intro{position:absolute;left:12px;top:138px;height:240px;font-size:11.5px;line-height:1.75;letter-spacing:1px}
.photo-tansu{left:100px;top:140px;width:550px;height:705px;background:linear-gradient(180deg,#3a0f12,var(--tansu) 45%,#2a0a0c);border-top:6px solid var(--iron);border-bottom:10px solid var(--iron)}
.title-main{position:absolute;left:664px;top:180px;font-family:"Yuji Syuku",serif;font-size:84px;line-height:1;color:var(--red)}
.title-sub{position:absolute;left:768px;top:540px;font-size:42px;font-weight:800;letter-spacing:4px;line-height:1}
.title-sub .gap{display:inline-block;height:18px}
.story{position:absolute;font-size:12px;line-height:1.8;letter-spacing:1px}
.story-head{position:absolute;color:var(--red);font-weight:700;font-size:20px;letter-spacing:3px;line-height:1}
.head-tradition{left:452px;top:868px}
.body-tradition{left:290px;top:868px;height:225px}
.head-craft{left:684px;top:868px;color:var(--ink);font-size:19px}
.body-craft{left:520px;top:868px;height:225px}
.photo-master{left:718px;top:912px;width:128px;height:183px;background:linear-gradient(170deg,#d9d2c4,#9c8c7c 50%,#4d4038)}
.footer{position:absolute;left:0;top:1100px;width:846px;height:100px;border-top:1px solid var(--line);display:flex;gap:36px;padding:18px 16px;font-size:12px;line-height:1.9}
.footer .block{flex:0 0 auto}
.footer .contact{width:250px}
.footer .web{width:240px}
.footer .url-space{display:inline-block;width:150px;border-bottom:1px solid var(--line)}
.footer .shop{font-weight:700}
</style>
</head>
<body>
  <div class="photo photo-urushi" role="img" aria-label="漆を塗る職人の手元の写真"></div>
  <div class="photo photo-kanagu" role="img" aria-label="金具を打ち出す職人の手元の写真"></div>
  <div class="photo photo-mokkou" role="img" aria-label="木材を削る職人の手元の写真"></div>

  <span class="craft-label label-urushi vertical">漆</span>
  <span class="craft-label label-kanagu vertical">金具</span>
  <span class="craft-label label-mokkou vertical">木工</span>

  <p class="intro vertical">仙台箪笥は、指物・漆塗・金具の三つの技が一つになって生まれる伝統の家具です。柴崎庵では全ての工程を手しごとで仕上げます。</p>

  <div class="photo photo-tansu" role="img" aria-label="鉄金具が施された赤漆塗りの仙台箪笥の写真"></div>

  <h1 class="title-main vertical">手しごと</h1>
  <h2 class="title-sub vertical">仙台箪笥<span class="gap"></span>柴崎庵</h2>

  <h3 class="story-head head-tradition vertical">百年先へ伝統を繋ぐ</h3>
  <p class="story body-tradition vertical">江戸時代から培われた仙台の技は、職人の手から手へと受け継がれてきました。機械では生まれない深い艶と確かな強さ。本物の箪笥は百年を超えて使い続けられ、次の世代への財産となります。その価値を、未来へ繋いでいきます。</p>

  <h3 class="story-head head-craft vertical">全ては「手しごと」で</h3>
  <p class="story body-craft vertical">木を選び、組み、漆を重ね、金具を一枚ずつ打ち出す。柴崎守は全ての工程を自らの手で行い、愚直に本物だけを作り続けています。</p>

  <div class="photo photo-master" role="img" aria-label="作業場に立つ職人 柴崎守氏の写真"></div>

  <footer class="footer">
    <div class="block contact">TEL 022-000-4817<br>FAX 022-000-4818</div>
    <div class="block web">E-mail info@shibasakian-demo.jp<br>URL <span class="url-space"></span></div>
    <div class="block address"><span class="shop">仙台箪笥 柴崎庵</span><br>〒980-0000 仙台市青葉区架空町一丁目2-3</div>
  </footer>
</body>
</html>
```